Business card required for IT Consultancy Business - Tealbrook Consulting.
Company provides the whole nine yards of services across IT Architecture, design and execution.
Basically we provide consulting services to help businesses make sure their technology is enabling their business strategy.
Design for front and back required.
We would like the front of the card to inlcude:
Name
Title
Mobile number
email address
www.tbkc.com.au
Company logos attached.
Thank you
Industry/Entity Type
Business
Contact Information for Business Card
Name
Title
Mobile number
email address
www.tbkc.com.au
Look and feel
Each slider illustrates characteristics of the customer's brand and the style your logo design should communicate.

```html
<!DOCTYPE html>
<html lang="en">
<head>
<meta charset="utf-8">
<title>Tealbrook Consulting – Business Card</title>
<link href="https://fonts.googleapis.com/css2?family=Arimo:wght@400;700&display=swap" rel="stylesheet">
<style>
  :root {
    --orange: #f05a2c;
    --blue: #1378c0;
    --white: #ffffff;
    --ink: #231f20;
    --grey-soft: #e4e4e4;
    --grey-fade: #f6f6f6;
    --card-border: #d9d9d9;
    --page: #ffffff;
  }
  * { margin: 0; padding: 0; box-sizing: border-box; }
  html, body {
    width: 974px; height: 1200px; overflow: hidden;
    background: var(--page);
    font-family: "Arimo", Arial, sans-serif;
    color: var(--ink);
  }
  .sheet { position: relative; width: 974px; height: 1200px; }
  .side-label {
    position: absolute; left: 126px;
    font-size: 24px; font-weight: 400; color: var(--ink);
  }
  .side-label--front { top: 90px; }
  .side-label--back { top: 600px; }
  .card {
    position: absolute; left: 108px; width: 758px; height: 433px;
    overflow: hidden;
  }
  .card--front { top: 139px; }
  .card--back { top: 650px; border: 1px solid var(--card-border); background: var(--white); }
  .card__art { position: absolute; inset: 0; width: 100%; height: 100%; }

  .front__brand {
    position: absolute; left: 300px; top: 190px; width: 260px;
    text-align: center; color: var(--white);
    font-size: 32px; font-weight: 700; line-height: 1.15;
  }
  .front__url {
    position: absolute; left: 38px; top: 366px;
    color: var(--white); font-size: 22px; letter-spacing: 1px;
  }

  .back__texture {
    position: absolute; right: 0; top: 0; width: 148px; height: 118px;
  }

  .back__identity { position: absolute; right: 56px; top: 132px; text-align: right; }
  .back__name { color: var(--orange); font-size: 32px; font-weight: 700; line-height: 1; }
  .back__title { font-size: 21px; margin-top: 4px; }

  .back__contacts { position: absolute; right: 56px; top: 270px; list-style: none; }
  .contact {
    display: flex; align-items: center; justify-content: flex-end;
    height: 45px; font-size: 21px; letter-spacing: 1.6px;
  }
  .contact__icon { width: 30px; height: 30px; margin-left: 24px; flex: none; }

  .back__brand {
    position: absolute; left: 44px; top: 340px;
    display: flex; align-items: center; gap: 10px;
    color: var(--blue); font-size: 23px; font-weight: 700;
  }
  .back__brand-dot { width: 22px; height: 22px; border-radius: 50%; background: var(--orange); }
</style>
</head>
<body>
<main class="sheet">
  <p class="side-label side-label--front">Front</p>
  <section class="card card--front" aria-label="Card front">
    <svg class="card__art" viewBox="0 0 758 433" aria-hidden="true">
      <rect width="758" height="433" fill="var(--orange)"/>
      <polygon points="666,0 758,0 758,433 488,433" fill="var(--white)"/>
      <polygon points="684,0 758,0 758,433 504,433" fill="var(--blue)"/>
    </svg>
    <p class="front__brand">Tealbrook<br>Consulting</p>
    <p class="front__url">www.tbkc.com.au</p>
  </section>

  <p class="side-label side-label--back">Back</p>
  <section class="card card--back" aria-label="Card back">
    <svg class="card__art" viewBox="0 0 758 433" aria-hidden="true">
      <polygon points="0,0 140,0 0,190" fill="var(--orange)"/>
      <polygon points="148,0 186,0 0,250 0,204" fill="var(--blue)"/>
    </svg>

    <svg class="back__texture" viewBox="0 0 148 118" role="img" aria-label="Decorative diagonal hatching in light grey">
      <defs>
        <linearGradient id="texture-fade" x1="1" y1="0" x2="0" y2="1">
          <stop offset="0" stop-color="var(--grey-soft)"/>
          <stop offset="1" stop-color="var(--grey-fade)"/>
        </linearGradient>
      </defs>
      <polygon points="58,0 148,0 148,30 82,118 54,118 82,80 0,76" fill="url(#texture-fade)"/>
    </svg>

    <div class="back__identity">
      <p class="back__name">Your Name</p>
      <p class="back__title">Title</p>
    </div>

    <ul class="back__contacts">
      <li class="contact">info@tbkc.com.au
        <svg class="contact__icon" viewBox="0 0 30 30" aria-hidden="true" fill="none" stroke="var(--blue)" stroke-width="1.8">
          <rect x="2" y="7" width="26" height="17"/>
          <polyline points="2,7 15,17 28,7"/>
          <line x1="2" y1="24" x2="12" y2="15"/><line x1="28" y1="24" x2="18" y2="15"/>
        </svg>
      </li>
      <li class="contact">0123 456 798
        <svg class="contact__icon" viewBox="0 0 30 30" aria-hidden="true" fill="none" stroke="var(--blue)" stroke-width="1.8">
          <rect x="7" y="1" width="16" height="28" rx="3"/>
          <rect x="10" y="5" width="10" height="18"/>
          <circle cx="15" cy="26" r="1" fill="var(--blue)"/>
        </svg>
      </li>
      <li class="contact">www.tbkc.com.au
        <svg class="contact__icon" viewBox="0 0 30 30" aria-hidden="true" fill="none" stroke="var(--blue)" stroke-width="1.8">
          <circle cx="15" cy="15" r="13"/>
          <ellipse cx="15" cy="15" rx="6" ry="13"/>
          <line x1="15" y1="2" x2="15" y2="28"/>
          <line x1="2" y1="15" x2="28" y2="15"/>
          <path d="M4 8 H26 M4 22 H26"/>
        </svg>
      </li>
    </ul>

    <div class="back__brand">
      <span class="back__brand-dot" aria-hidden="true"></span>
      <span>Tealbrook Consulting</span>
    </div>
  </section>
</main>
</body>
</html>
```